New Sticker Design Project

Hello, Thank you for the great design of the tape. I would like to hire you to create another design to match the tape for the side of the box. 4" X 6"
Text: Perishable, Living Food as Medicine, Please Keep Cold, Do Not Delay, Quick Delivery Necessary, Place in Refrigerator Immediately upon Delivery
With symbols for Cold, and time-sensitive. Could use all caps if the design looks good. Same text font and color scheme to match the look of the tape. Logo if space. This needs to stand out on the shipping box which is brown boxes. Thanks again. !
Target Market(s)
Shipping box informational Sticker Outside
Requirements
Must have
- Similar matching look to the tape. The word PERISHABLE needs to be dominate!
Nice to have
- bold easy to read eye catching information for Parzo and customer
Should not have
- Clutter

```html
<!DOCTYPE html>
<html lang="en">
<head>
<meta charset="utf-8">
<title>Verdant Tide Algae – Perishable Shipping Sticker</title>
<link rel="stylesheet" href="https://fonts.googleapis.com/css2?family=Jost:wght@600;700&display=swap">
<style>
  :root {
    --page: #ffffff;
    --ink: #3a3a3a;
    --frame: #2b2b2b;
    --accent: #1f8a78;
  }
  * { box-sizing: border-box; margin: 0; padding: 0; }
  html, body {
    width: 694px;
    height: 1200px;
    overflow: hidden;
    background: var(--page);
    font-family: "Jost", "Futura", sans-serif;
    color: var(--ink);
  }
  .sticker {
    position: absolute;
    left: 53px;
    top: 404px;
    width: 588px;
    height: 392px;
    border: 2.5px solid var(--frame);
    border-radius: 40px;
  }
  .brand {
    position: absolute;
    top: 18px;
    left: 0;
    width: 100%;
    text-align: center;
  }
  .brand-mark {
    display: block;
    width: 38px;
    height: 38px;
    margin: 0 auto 6px;
    border-radius: 50%;
    background: var(--accent);
  }
  .brand-name {
    font-weight: 700;
    font-size: 38px;
    line-height: 38px;
    letter-spacing: -0.5px;
    color: var(--ink);
  }
  .notice {
    position: absolute;
    display: flex;
    align-items: center;
    gap: 20px;
  }
  .notice svg {
    flex: 0 0 auto;
    width: 44px;
    height: 44px;
    fill: none;
    stroke: var(--ink);
    stroke-width: 2;
    stroke-linecap: round;
    stroke-linejoin: round;
  }
  .notice-label {
    font-weight: 700;
    font-size: 17.5px;
    line-height: 24px;
    letter-spacing: 0.2px;
  }
  .notice--perishable { left: 42px; top: 162px; }
  .notice--delay { left: 42px; top: 222px; }
  .notice--delivery { left: 42px; top: 290px; }
  .notice--cold { left: 312px; top: 160px; }
  .notice--medicine { left: 312px; top: 220px; }
  .notice--fridge { left: 312px; top: 290px; }
  .notice--fridge { align-items: flex-start; }
  .notice--fridge svg { margin-top: 4px; }
</style>
</head>
<body>
  <section class="sticker" aria-label="Perishable shipping sticker">
    <header class="brand">
      <span class="brand-mark" aria-hidden="true"></span>
      <h1 class="brand-name">VERDANT TIDE<br>ALGAE</h1>
    </header>

    <div class="notice notice--perishable">
      <svg viewBox="0 0 44 44" aria-hidden="true">
        <rect x="4" y="2" width="6" height="5"/>
        <rect x="3" y="7" width="8" height="20" rx="2"/>
        <path d="M8 22h30l-3 10H11z"/>
        <circle cx="10" cy="36" r="6"/>
        <path d="M20 36l16-6 4 3-18 8z"/>
        <path d="M16 22c0-6 4-10 8-10s8 4 8 10"/>
      </svg>
      <span class="notice-label">Perishable</span>
    </div>

    <div class="notice notice--delay">
      <svg viewBox="0 0 44 44" aria-hidden="true">
        <circle cx="19" cy="19" r="16"/>
        <circle cx="19" cy="19" r="12"/>
        <path d="M19 11v8h-4"/>
        <circle cx="32" cy="33" r="9" fill="#fff"/>
        <path d="M32 28v6"/>
        <circle cx="32" cy="38" r="0.8"/>
      </svg>
      <span class="notice-label">Do Not Delay</span>
    </div>

    <div class="notice notice--delivery">
      <svg viewBox="0 0 44 44" aria-hidden="true">
        <path d="M14 10h18v22H14"/>
        <path d="M32 16h6l5 8v8h-11"/>
        <path d="M35 18v6h7"/>
        <circle cx="18" cy="34" r="4"/>
        <circle cx="36" cy="34" r="4"/>
        <path d="M2 16h10M5 22h8M2 28h8M2 34h10"/>
      </svg>
      <span class="notice-label">Quick Delivery<br>Necessary</span>
    </div>

    <div class="notice notice--cold">
      <svg viewBox="0 0 44 44" aria-hidden="true">
        <path d="M22 3v38M6 12l32 20M6 32l32-20"/>
        <path d="M18 6l4 4 4-4M18 38l4-4 4 4"/>
        <path d="M5 17l6-1-1-6M39 27l-6 1 1 6"/>
        <path d="M5 27l6 1-1 6M39 17l-6-1 1-6"/>
        <path d="M22 16l5 3v6l-5 3-5-3v-6z"/>
      </svg>
      <span class="notice-label">Please Keep Cold</span>
    </div>

    <div class="notice notice--medicine">
      <svg viewBox="0 0 44 44" aria-hidden="true">
        <circle cx="22" cy="24" r="17"/>
        <ellipse cx="16" cy="10" rx="4" ry="5"/>
        <path d="M16 15v20"/>
        <path d="M26 4v8a3 3 0 0 0 6 0V4M29 12v23"/>
        <path d="M8 36c4-1 7 1 9 4M36 36c-4-1-7 1-9 4"/>
      </svg>
      <span class="notice-label">Living Food as<br>Medicine</span>
    </div>

    <div class="notice notice--fridge">
      <svg viewBox="0 0 44 44" aria-hidden="true">
        <rect x="8" y="2" width="28" height="40" rx="1"/>
        <path d="M22 2v40M8 30h28"/>
        <rect x="12" y="12" width="6" height="7"/>
        <path d="M20 10v8M24 10v8"/>
      </svg>
      <span class="notice-label">Place in Refrigerator<br>Immediately upon<br>Delivery</span>
    </div>
  </section>
</body>
</html>
```